Interactive Tailored Suit and Shirt Website Needs Homepage Redesign

We need our homepage redesigned. Our current website is dated and we need a refresh. We are a Melbourne based business selling tailored suits and shirts in store and online. The homepage should be fashion forward. Our colour scheme has traditionally been black and white but would interested in new ideas.
Our current website is larimvox.com.au

```html
<!DOCTYPE html>
<html lang="en">
<head>
<meta charset="utf-8">
<title>larimvox — Tailored Suits &amp; Shirts</title>
<link rel="stylesheet" href="https://fonts.googleapis.com/css2?family=Ubuntu:wght@400;500;700&display=swap">
<style>
:root{
  --black:#000;
  --white:#fff;
  --nav-text:#d2d2d2;
  --nav-active:#8a8a8a;
  --page-top:#f8f7f5;
  --page-bottom:#d8d1bf;
  --frame-fill:#dcdcdc;
  --photo-dark:#3c3c3c;
  --photo-mid:#6e6e6e;
  --band:#675a58;
  --field:#3e3433;
  --field-text:#5e5352;
  --social-pill:#2a2a2a;
  --social-edge:#555;
}
*{margin:0;padding:0;box-sizing:border-box}
html,body{width:1200px;height:1200px;overflow:hidden}
body{position:relative;font-family:"Ubuntu",sans-serif;background:linear-gradient(var(--page-top) 172px,var(--page-bottom) 960px)}
.abs{position:absolute}

.site-header{left:0;top:0;width:1200px;height:172px;background:var(--black)}
.brand{left:55px;top:60px;font-size:36px;font-weight:500;color:var(--white);letter-spacing:-.5px}
.nav-link{top:90px;font-size:17px;color:var(--nav-text)}
.nav-link.active{color:var(--nav-active)}
.social-pill{left:973px;top:63px;width:240px;height:58px;border-radius:29px;background:var(--social-pill);border:3px solid var(--social-edge)}
.social-dot{top:72px;width:42px;height:42px;border-radius:50%}

.side-frame{border:2px solid var(--black);background:var(--white)}
.slider-frame{left:192px;top:258px;width:827px;height:409px;border:3px solid var(--black);background:var(--frame-fill);box-shadow:0 18px 22px -10px rgba(0,0,0,.25)}
.slider-photo{left:205px;top:271px;width:800px;height:378px;border:3px solid var(--black);background:radial-gradient(ellipse at 55% 40%,var(--photo-mid),var(--photo-dark) 80%)}
.cta{left:612px;top:507px;width:378px;height:127px;background:rgba(150,150,150,.75);border:2px solid rgba(200,200,200,.6)}
.cta-small{left:642px;top:532px;font-size:28px;color:var(--white);text-shadow:1px 1px 2px #000}
.cta-large{left:642px;top:570px;font-size:36px;font-weight:500;color:var(--white);text-shadow:1px 2px 3px #000}
.pager-dot{top:616px;width:19px;height:19px;border-radius:50%;background:var(--white);border:3px solid var(--black)}
.pager-dot.current{background:var(--black)}

.feature{top:766px;font-size:17px;font-weight:500;color:var(--black);transform:translateX(-50%)}
.feature-rule{top:744px;width:3px;height:84px;border-left:1px solid #000;border-right:1px solid #000}

.subscribe{left:0;top:960px;width:1200px;height:132px;background:var(--band);border-top:2px solid var(--white)}
.subscribe-title{left:0;width:1210px;top:977px;text-align:center;font-size:23px;font-weight:500;color:var(--white)}
.email-field{left:211px;top:1018px;width:630px;height:55px;background:var(--field);border-radius:3px;box-shadow:inset 0 0 14px #000;font-size:23px;color:var(--field-text);padding:13px 20px}
.submit-btn{left:855px;top:1016px;width:154px;height:56px;background:#161313;border:2px solid #8a7f7c;border-radius:4px;font-size:23px;font-weight:500;color:#3a3332;text-align:center;line-height:52px}
.envelope{left:124px;top:974px;width:96px;height:92px;background:linear-gradient(#7cc3ea 45%,#eef2f4 45%);border-radius:6px;transform:rotate(-12deg)}

.site-footer{left:0;top:1092px;width:1200px;height:108px;background:var(--black)}
.foot-link{font-size:17px;color:var(--white)}
.copyright{left:0;width:1264px;top:1176px;text-align:center;font-size:17px;color:var(--white)}
</style>
</head>
<body>
<header class="abs site-header"></header>
<div class="abs brand">larimvox</div>
<nav>
  <span class="abs nav-link" style="left:306px">Customize Your Own</span>
  <span class="abs nav-link active" style="left:554px;top:92px">LookBook</span>
  <span class="abs nav-link" style="left:722px;top:92px">My Larimvox</span>
</nav>
<div class="abs social-pill"></div>
<span class="abs social-dot" style="left:990px;background:#3b5bab"></span>
<span class="abs social-dot" style="left:1042px;background:#111"></span>
<span class="abs social-dot" style="left:1095px;background:#1487c4"></span>
<span class="abs social-dot" style="left:1146px;background:#4a9de0"></span>

<div class="abs side-frame" style="left:160px;top:294px;width:40px;height:341px"></div>
<div class="abs side-frame" style="left:174px;top:305px;width:26px;height:315px"></div>
<div class="abs side-frame" style="left:1010px;top:294px;width:39px;height:341px"></div>
<div class="abs side-frame" style="left:1010px;top:305px;width:26px;height:315px"></div>

<svg class="abs" style="left:88px;top:415px" width="60" height="75" aria-label="Previous slide">
  <g fill="#000"><circle cx="44" cy="12" r="7"/><circle cx="26" cy="22" r="7"/><circle cx="11" cy="37" r="7"/><circle cx="24" cy="52" r="7"/><circle cx="41" cy="65" r="7"/></g>
</svg>
<svg class="abs" style="left:1062px;top:437px" width="60" height="75" aria-label="Next slide">
  <g fill="#000"><circle cx="16" cy="13" r="7"/><circle cx="35" cy="23" r="7"/><circle cx="50" cy="38" r="7"/><circle cx="36" cy="52" r="7"/><circle cx="19" cy="66" r="7"/></g>
</svg>

<div class="abs slider-frame"></div>
<div class="abs slider-photo" role="img" aria-label="Model wearing a dark pinstripe three-piece suit against a grey backdrop"></div>
<div class="abs cta"></div>
<div class="abs cta-small">Book an</div>
<div class="abs cta-large">Appointment</div>
<svg class="abs" style="left:906px;top:560px" width="58" height="62" aria-hidden="true">
  <polygon points="4,4 28,4 54,31 28,58 4,58 30,31" fill="#fff" stroke="#888" stroke-width="1"/>
</svg>
<span class="abs pager-dot" style="left:228px"></span>
<span class="abs pager-dot" style="left:264px"></span>
<span class="abs pager-dot current" style="left:300px"></span>
<span class="abs pager-dot" style="left:336px"></span>
<span class="abs pager-dot" style="left:372px"></span>

<div class="abs feature" style="left:298px">YOUR DESIGN</div>
<div class="abs feature-rule" style="left:436px"></div>
<div class="abs feature" style="left:576px;top:768px">PERFECT FIT</div>
<div class="abs feature-rule" style="left:742px"></div>
<div class="abs feature" style="left:920px;top:760px">GUARANTEED</div>

<section class="abs subscribe"></section>
<div class="abs subscribe-title">SUBSCRIBE TO OUR LATEST NEWS AND EXCLUSIVE OFFERS</div>
<div class="abs email-field">Enter your Email Address</div>
<div class="abs submit-btn">SUBMIT</div>
<div class="abs envelope" role="img" aria-label="Envelope with letter icon"></div>

<footer class="abs site-footer"></footer>
<a class="abs foot-link" style="left:99px;top:1101px">Home</a>
<a class="abs foot-link" style="left:99px;top:1131px">Customize your own</a>
<a class="abs foot-link" style="left:358px;top:1104px">LookBook</a>
<a class="abs foot-link" style="left:358px;top:1134px">About Larimvox</a>
<a class="abs foot-link" style="left:612px;top:1110px">My Larimvox</a>
<a class="abs foot-link" style="left:612px;top:1142px">FAQ</a>
<a class="abs foot-link" style="left:870px;top:1108px">T&amp;C</a>
<a class="abs foot-link" style="left:870px;top:1140px">Contact Us</a>
<div class="abs copyright">© 2012-2013 LARIMVOX. All Right Reserved. Tarnel Softworks.</div>
</body>
</html>
```